Interior Stylist business card design needed

I need a business card for my new company in Sydney called "Pip Dunstane Designs". The business offers an interior styling and colour consultancy. My clients are generally not very design savvy (hence why they use me) and can range from being quite conservative to really wanting something "out there". They can be looking for a budget makeover or something more expensive / substantial. I'd like my business card design to be stylish (but not overly formal). I certainly don't want it to be conservative. I'd like it to stand out a bit! I don't really have any aversion to particular colours and I don't have a logo as such - my business name is really all I have.

Target Market(s)

As above - home owners, ranging from conservative to modern

Industry/Entity Type

Conservative

Contact Information for Business Card

Pip Dunstane Designs
Colour consultancy and interior styling
ph: 0417 382 605
email: pipdunstane@harvolink.net.au

Requirements
Should not have
• Old fashioned writing or motifs. No Times Roman font!!

```html
<!DOCTYPE html>
<html lang="en">
<head>
<meta charset="utf-8">
<title>Pip Dunstane Designs – Business Card</title>
<link rel="stylesheet" href="https://fonts.googleapis.com/css2?family=Marcellus&family=Open+Sans:wght@400&display=swap">
<style>
  :root {
    --bg: #ece9e2;
    --charcoal: #424143;
    --stone: #c8c4a6;
    --cream: #e6e1c7;
    --ink: #3a393b;
    --shadow: rgba(0, 0, 0, 0.18);
  }
  * { margin: 0; padding: 0; box-sizing: border-box; }
  html, body { width: 1200px; height: 787px; overflow: hidden; background: var(--bg); }
  .stage { position: relative; width: 1200px; height: 787px; }

  .card {
    position: absolute;
    width: 520px;
    height: 300px;
    box-shadow: 0 10px 24px var(--shadow);
  }
  .card svg.card-shape { position: absolute; inset: 0; width: 100%; height: 100%; }

  /* Front: name card */
  .card--front { left: 620px; top: 90px; }
  .card--front .wordmark {
    position: absolute; left: 0; right: 30px; top: 118px;
    text-align: center;
    font-family: "Marcellus", sans-serif;
    font-size: 30px; letter-spacing: 3px;
    color: var(--cream);
  }
  .card--front .web {
    position: absolute; left: 0; right: 30px; top: 176px;
    text-align: center;
    font-family: "Open Sans", sans-serif;
    font-size: 12px; letter-spacing: 0.5px;
    color: var(--cream);
  }

  /* Back: contact card */
  .card--back { left: 70px; top: 400px; }
  .card--back .wordmark {
    position: absolute; right: 40px; top: 62px;
    text-align: center;
    font-family: "Marcellus", sans-serif;
    color: var(--cream);
  }
  .card--back .wordmark .name { font-size: 28px; letter-spacing: 3px; display: block; }
  .card--back .wordmark .tag { font-size: 13px; letter-spacing: 9px; display: block; margin-top: 4px; }

  .contact {
    position: absolute; left: 22px; top: 182px;
    list-style: none;
    font-family: "Open Sans", sans-serif;
    font-size: 12px; color: var(--ink);
  }
  .contact li { display: flex; align-items: center; gap: 8px; height: 19px; }
  .contact .icon { width: 12px; height: 12px; flex: none; }
</style>
</head>
<body>
<main class="stage">

  <section class="card card--front" aria-label="Business card front">
    <svg class="card-shape" viewBox="0 0 520 300" preserveAspectRatio="none">
      <rect width="520" height="300" fill="var(--stone)"/>
      <path d="M0 0 H496 L492 40 L498 90 L490 160 L494 230 L488 272 L440 276 L360 272 L260 278 L150 274 L60 279 L0 276 Z" fill="var(--charcoal)"/>
      <line x1="30" y1="10" x2="470" y2="12" stroke="var(--stone)" stroke-width="1" opacity="0.5"/>
    </svg>
    <div class="wordmark">PIP DUNSTANE</div>
    <div class="web">www.pipdunstane.com</div>
  </section>

  <section class="card card--back" aria-label="Business card back">
    <svg class="card-shape" viewBox="0 0 520 300" preserveAspectRatio="none">
      <rect width="520" height="300" fill="var(--charcoal)"/>
      <path d="M0 168 L210 172 L300 182 L360 200 L430 226 L520 246 V272 H0 Z" fill="var(--stone)"/>
      <path d="M260 180 L420 214 L520 236" stroke="var(--stone)" stroke-width="1.5" fill="none"/>
    </svg>
    <div class="wordmark">
      <span class="name">PIP DUNSTANE</span>
      <span class="tag">DESIGNS</span>
    </div>
    <ul class="contact">
      <li>
        <svg class="icon" viewBox="0 0 12 12" aria-hidden="true"><rect width="12" height="12" rx="2" fill="var(--charcoal)"/><path d="M3.5 2.5 L5 4.5 L4.2 5.4 Q5 7 6.6 7.8 L7.5 7 L9.5 8.5 L8.6 9.6 Q5.5 9.5 2.5 3.4 Z" fill="var(--cream)"/></svg>
        <span>0417 382 605</span>
      </li>
      <li>
        <svg class="icon" viewBox="0 0 12 12" aria-hidden="true"><rect width="12" height="12" rx="2" fill="var(--charcoal)"/><rect x="2.5" y="3.5" width="7" height="5" fill="none" stroke="var(--cream)" stroke-width="0.9"/><path d="M2.5 3.5 L6 6.5 L9.5 3.5" fill="none" stroke="var(--cream)" stroke-width="0.9"/></svg>
        <span>pipdunstane@harvolink.net.au</span>
      </li>
      <li>
        <svg class="icon" viewBox="0 0 12 12" aria-hidden="true"><rect width="12" height="12" rx="2" fill="var(--charcoal)"/></svg>
        <span>www.friendpage.net/pipdunstane</span>
      </li>
    </ul>
  </section>

</main>
</body>
</html>
```